Plume Ovenworks, need a business card design for an innovative bakery

This is a new company out of Boston. We develop innovative baking products. I would you to make a simple card with the colors attached. The design should be modern and fun. Our tag line is " The kindest way to share". This should be incorporated into the design.

Industry/Entity Type

Business

Contact Information for Business Card

Plume Ovenworks LLC

Font styles to use
Sans Serif

Requirements
Must have
• Felix Marrow
• Address: 818 Tindle Ave, Suite 2190, Alderbrook MA, 01987
• Phone: 617-5930268
• Emial: FelixMarrow@plumeovenworks.example

```html
<!DOCTYPE html>
<html lang="en">
<head>
<meta charset="utf-8">
<title>Plume Ovenworks – Business Card</title>
<link rel="stylesheet" href="https://fonts.googleapis.com/css2?family=Marcellus&family=Crimson+Text&display=swap">
<style>
  :root {
    --page: #e9e4dc;
    --navy: #1c2a48;
    --ocean: #0f3a5e;
    --aqua: #97dfdd;
    --silver: #cfd3da;
    --tagline: #bfe2e2;
    --name: #a6e3e2;
    --contact: #d6e5ee;
    --rule: #c8ccd4;
  }
  * { margin: 0; padding: 0; box-sizing: border-box; }
  html, body { width: 1200px; height: 970px; overflow: hidden; background: var(--page); }
  .canvas { position: relative; width: 1200px; height: 970px; }
  .card {
    position: absolute; left: 100px; top: 207px;
    width: 1000px; height: 556px;
    border-radius: 18px; overflow: hidden;
    background: var(--navy);
    box-shadow: 0 10px 30px rgba(0,0,0,0.18);
  }
  .card-shapes { position: absolute; inset: 0; }
  .brand-name {
    position: absolute; left: 285px; width: 438px; top: 148px;
    text-align: center; white-space: nowrap;
    font-family: "Marcellus", serif; font-size: 46px; line-height: 68px;
    color: var(--silver); letter-spacing: 1px;
  }
  .tagline {
    position: absolute; left: 0; width: 1000px; top: 266px;
    text-align: center; white-space: nowrap;
    font-family: "Marcellus", serif; font-size: 20px;
    letter-spacing: 2.5px; color: var(--tagline);
  }
  .person-name {
    position: absolute; left: 78px; top: 418px;
    font-family: "Marcellus", serif; font-size: 52px;
    color: var(--name); white-space: nowrap;
  }
  .divider {
    position: absolute; left: 457px; top: 397px;
    width: 2px; height: 116px; background: var(--rule); opacity: 0.8;
  }
  .contact {
    position: absolute; left: 488px;
    display: flex; align-items: center; gap: 14px;
    font-family: "Crimson Text", serif; font-size: 23px;
    color: var(--contact); white-space: nowrap;
  }
  .contact svg { width: 22px; height: 22px; flex: none; }
  .contact-phone { top: 398px; }
  .contact-email { top: 430px; }
  .contact-address { top: 486px; font-size: 21px; }
</style>
</head>
<body>
<div class="canvas">
  <div class="card">
    <svg class="card-shapes" width="1000" height="556" viewBox="0 0 1000 556">
      <rect x="0" y="143" width="285" height="78" fill="var(--aqua)"/>
      <rect x="723" y="143" width="277" height="78" fill="var(--aqua)"/>
      <path d="M0 362 Q500 296 1000 362 L1000 556 L0 556 Z" fill="var(--ocean)"/>
      <path d="M0 362 Q500 296 1000 362" fill="none" stroke="var(--silver)" stroke-width="3"/>
    </svg>

    <div class="brand-name">Plume Ovenworks</div>
    <div class="tagline">" THE KINDEST WAY TO SHARE"</div>

    <div class="person-name">Felix Marrow</div>
    <div class="divider"></div>

    <div class="contact contact-phone">
      <svg viewBox="0 0 22 22" aria-hidden="true">
        <rect x="1" y="1" width="20" height="20" rx="4" fill="var(--contact)"/>
        <path d="M7 5.5c.8-.5 1.5-.3 1.9.4l1 1.8c.3.6.2 1.2-.3 1.6l-.8.6c.6 1.4 1.8 2.6 3.2 3.2l.6-.8c.4-.5 1-.6 1.6-.3l1.8 1c.7.4.9 1.1.4 1.9-.7 1.1-1.9 1.6-3.1 1.2-3.5-1.1-6.2-3.8-7.3-7.3-.4-1.2.1-2.4 1-3.3z" fill="var(--ocean)"/>
      </svg>
      <span>617-593-0268</span>
    </div>
    <div class="contact contact-email">
      <svg viewBox="0 0 22 22" aria-hidden="true">
        <rect x="2" y="4" width="18" height="14" rx="1.5" fill="var(--contact)"/>
        <path d="M3 5.5 L11 12 L19 5.5" fill="none" stroke="var(--ocean)" stroke-width="2"/>
      </svg>
      <span>FelixMarrow@plumeovenworks.example</span>
    </div>
    <div class="contact contact-address">
      <span>818 Tindle Ave, Suite 2190, Alderbrook MA, 01987</span>
    </div>
  </div>
</div>
</body>
</html>
```